Tallpine Facility Upkeep Systems

I need a full website built that must work on destkop and mobile. I have the logo's and will upload them however some stock industrial photos will be required. I will be hosting it on wix/godaddy for use with dynamics 365. Pretty simple requirements:

*Splash page
*What We Do
*How We do it
*Who Are We?
*Software
*Partnerships
*Contact: Includes twitter/insta and email/addy/phone

The site should be more scroll oriented with fewer tabs to allow for a improved mobile experience.
We're also looking for ways to improve our inbound marketing and would want to include various areas to get in touch /or collect their info. Look to www.kelnarova.com as an example of inbound marketing.
Images should be representative of the verticals we're focused on.

I have most of the content.

Target Market(s)

Asset intensive industries: Mining, Oil and Gas, Forest Products and Manufacturing.

Industry/Entity Type

Asset Management

Coding

Coded - Design and coding required

Number of Pages Required

5+ page

Font styles to use
Sans Serif

Requirements
Must have
• Must be easy to view and navigate on mobile and desktop.
Nice to have
• Employee/Customer portal.
Should not have
• Anything that will not display well in a mobile environment.

```html
<!DOCTYPE html>
<html lang="en">
<head>
<meta charset="utf-8">
<title>Tallpine Facility Upkeep Systems — Project Approach</title>
<link rel="stylesheet" href="https://fonts.googleapis.com/css2?family=Raleway:wght@400;500;600;700&family=Roboto+Condensed:wght@400&family=Open+Sans:wght@400;700&family=Arimo:wght@400;700&display=swap">
<style>
:root{
  --navy:#0f4a6b;
  --brand-green:#8aa04a;
  --ink:#222;
  --text:#444;
  --band:#f3f3f3;
  --rule:#999;
  --hero-top:#6fb3df;
  --hero-bottom:#2f8ccf;
  --footer:#3a3a3c;
  --footer-text:#e6e6e6;
  --accent:#3c6fa3;
  --ring:#1ca4dd;
  --icon-ring:#888;
  --icon-fill-a:#d4d4d4;
  --icon-fill-b:#9a9a9a;
}
*{box-sizing:border-box;margin:0;padding:0}
html,body{width:707px;height:1200px;overflow:hidden;background:#fff}
body{font-family:"Raleway",sans-serif;color:var(--text)}
.page{position:relative;width:707px;height:1200px;overflow:hidden}

/* header */
.site-header{position:absolute;left:0;top:0;width:707px;height:44px;background:#fff}
.brand{position:absolute;left:80px;top:11px;display:flex;align-items:center;gap:6px;font-size:14px;font-weight:600;color:var(--navy);letter-spacing:.5px}
.brand-dot{width:9px;height:9px;border-radius:50%;background:var(--brand-green)}
.main-nav{position:absolute;left:234px;top:14px;display:flex;font-size:8px;letter-spacing:.3px}
.main-nav a{color:#333;text-decoration:none;padding:3px 7px;line-height:9px}
.main-nav a.active{background:var(--navy);color:#fff;padding:3px 10px}

/* hero */
.hero{position:absolute;left:0;top:44px;width:707px;height:300px;
  background:linear-gradient(160deg,var(--hero-top),var(--hero-bottom));
  clip-path:polygon(0 0,100% 0,100% 81%,50% 100%,0 81%)}
.hero-title{position:absolute;left:80px;top:114px;font-size:21px;font-weight:700;color:#fff}
.hero-sub{position:absolute;left:81px;top:140px;width:260px;font-size:9.5px;font-weight:700;color:#fff;line-height:13px}

/* headings */
.section-title{position:absolute;left:0;width:707px;text-align:center;font-size:19px;font-weight:700;color:var(--ink)}

.intro{position:absolute;left:100px;top:402px;width:507px;text-align:center;font-size:7.8px;line-height:12.3px;color:var(--text);white-space:nowrap}

/* events */
.events{position:absolute;left:0;top:478px;width:707px;height:228px;background:var(--band)}
.event-photo{position:absolute;width:110px;height:119px}
.photo-chart{background:linear-gradient(135deg,#d9c45a,#b8b070 50%,#e6dfa0)}
.photo-calc{background:linear-gradient(135deg,#7fa3c8,#b8c4d0 50%,#8b9fb8)}
.event-meta{position:absolute;width:148px;height:16px;border-top:1px solid var(--rule);border-bottom:1px solid var(--rule);display:flex;align-items:center;gap:10px;font-family:"Arimo",sans-serif;font-size:6.8px;color:#444;padding-left:3px}
.event-meta span{display:flex;align-items:center;gap:3px}
.event-title{position:absolute;font-size:10.4px;font-weight:700;color:var(--ink)}
.event-text{position:absolute;font-family:"Arimo",sans-serif;font-size:6.9px;line-height:11.3px;color:#444;white-space:nowrap}
.read-more{position:absolute;display:flex;align-items:center;gap:3px;font-family:"Arimo",sans-serif;font-size:6.8px;font-weight:700;color:#333}

/* approach */
.approach-icon{position:absolute;width:70px;height:70px;border-radius:50%;border:1.5px solid var(--icon-ring);background:#fff;padding:8px}
.approach-icon span{display:block;width:100%;height:100%;border-radius:50%;background:radial-gradient(circle at 40% 35%,var(--icon-fill-a),var(--icon-fill-b))}
.approach-title{position:absolute;font-family:"Roboto Condensed",sans-serif;font-size:11.2px;color:var(--ink)}
.approach-list{position:absolute;width:76px;list-style:none;font-family:"Arimo",sans-serif;font-size:6.4px;color:#333}
.approach-list li{height:14px;line-height:13px;border-bottom:1px solid #888;padding-left:2px}
.approach-list li:last-child{border-bottom:none}

/* testimonials */
.testimonials{position:absolute;left:0;top:880px;width:707px;height:158px;background:var(--band)}
.avatar{position:absolute;left:169px;top:933px;width:70px;height:70px;border-radius:50%;border:3px solid var(--ring);background:linear-gradient(160deg,#9fc7d8,#c79a7a 55%,#3b8fb8)}
.quote{position:absolute;left:250px;top:942px;font-size:9px;line-height:12.5px;color:#444;white-space:nowrap}
.quote-author{position:absolute;left:251px;top:985px;font-family:"Open Sans",sans-serif;font-size:8.5px;font-weight:700;color:var(--ink)}

/* footer */
.site-footer{position:absolute;left:0;top:1038px;width:707px;height:162px;background:var(--footer);color:var(--footer-text)}
.footer-heading{position:absolute;top:12px;font-size:10px;font-weight:500;letter-spacing:.5px;padding-bottom:4px;border-bottom:1px solid #5a5a5c;width:78px}
.quick-links{position:absolute;left:97px;top:34px;list-style:none;font-size:7px;letter-spacing:.3px;line-height:12.4px}
.address-row{position:absolute;display:flex;align-items:flex-start;gap:9px;font-size:7.3px;line-height:11px}
.newsletter-note{position:absolute;left:456px;top:38px;font-family:"Arimo",sans-serif;font-size:7px}
.subscribe{position:absolute;left:456px;top:53px;display:flex;height:20px}
.subscribe-input{width:108px;background:#fff;color:#999;font-size:7.5px;padding:5px 7px}
.subscribe-btn{width:51px;background:var(--accent);color:#fff;font-family:"Open Sans",sans-serif;font-size:8px;font-weight:700;display:flex;align-items:center;justify-content:center}
.social{position:absolute;top:91px;width:16px;height:16px;border-radius:50%}
.copyright{position:absolute;left:95px;top:143px;font-family:"Open Sans",sans-serif;font-size:6px;border-top:1px solid #555;width:518px;padding-top:6px}
.to-top{position:absolute;left:599px;top:1027px;width:19px;height:19px}
</style>
</head>
<body>
<div class="page">

  <header class="site-header">
    <div class="brand"><span class="brand-dot"></span>Tallpine</div>
    <nav class="main-nav">
      <a class="active">Home</a><a>What We Do</a><a>How We do it</a><a>Who Are We?</a><a>Software</a><a>Partnerships</a><a>Contact</a>
    </nav>
  </header>

  <section class="hero" role="img" aria-label="Photo of hands reviewing bar charts on a clipboard beside a calculator, blue tint"></section>
  <h1 class="hero-title">PROJECT APPROACH</h1>
  <p class="hero-sub">Your placeholder text: Lorem ipsum dolor sit amet consectetur adipiscing elit.</p>

  <h2 class="section-title" style="top:367px">Who We Are</h2>
  <p class="intro">Tallpine Facility Upkeep Systems is a boutique firm specializing in maintenance and reliability, supply chain, business intelligence<br>and program management for asset intensive industries.<br>We represent the finest people, process and technology tools to achieve greater results.</p>

  <section class="events">
    <h2 class="section-title" style="top:12px">Tallpine Events</h2>

    <div class="event-photo photo-chart" style="left:80px;top:65px" role="img" aria-label="Illustration of figures assembling a colourful pie chart"></div>
    <div class="event-meta" style="left:195px;top:65px">
      <span><svg width="8" height="8" viewBox="0 0 8 8"><rect x=".5" y="1.5" width="7" height="6" fill="none" stroke="#444"/><path d="M.5 3h7M2.5 .5v2M5.5 .5v2" stroke="#444"/></svg>03 Jan</span>
      <span><svg width="6" height="8" viewBox="0 0 6 8"><path d="M3 8C1 5 0 4 0 3a3 3 0 0 1 6 0c0 1-1 2-3 5z" fill="#444"/><circle cx="3" cy="3" r="1" fill="#f3f3f3"/></svg>Lorem ipsum dolor sit amet</span>
    </div>
    <h3 class="event-title" style="left:196px;top:86px">Lorem ipsum dolor sit amet</h3>
    <p class="event-text" style="left:196px;top:100px">Lorem ipsum dolor sit amet, consectetuer adipi-<br>scing elit. Aenean commodo ligula eget dolor.<br>Aenean massa. Cum sociis natoque penatibus<br>et magnis dis parturient montes, nascetur<br>montes, nascetur ridiculus Lorem</p>
    <div class="read-more" style="left:197px;top:160px"><svg width="7" height="7" viewBox="0 0 8 8"><circle cx="4" cy="4" r="3.4" fill="none" stroke="#333"/><path d="M2 4h4M4.3 2.5 6 4 4.3 5.5" fill="none" stroke="#333"/></svg>Read More</div>

    <div class="event-photo photo-calc" style="left:365px;top:65px" role="img" aria-label="Photo of a calculator next to glasses and a tablet"></div>
    <div class="event-meta" style="left:479px;top:65px">
      <span><svg width="8" height="8" viewBox="0 0 8 8"><rect x=".5" y="1.5" width="7" height="6" fill="none" stroke="#444"/><path d="M.5 3h7M2.5 .5v2M5.5 .5v2" stroke="#444"/></svg>03 Jan</span>
      <span><svg width="6" height="8" viewBox="0 0 6 8"><path d="M3 8C1 5 0 4 0 3a3 3 0 0 1 6 0c0 1-1 2-3 5z" fill="#444"/><circle cx="3" cy="3" r="1" fill="#f3f3f3"/></svg>Lorem ipsum dolor sit amet</span>
    </div>
    <h3 class="event-title" style="left:480px;top:86px">Lorem ipsum dolor sit amet</h3>
    <p class="event-text" style="left:480px;top:100px">Lorem ipsum dolor sit amet, consectetuer adipi-<br>scing elit. Aenean commodo ligula eget dolor.<br>Aenean massa. Cum sociis natoque penatibus<br>et magnis dis parturient montes, nascetur<br>montes, nascetur ridiculus Lorem</p>
    <div class="read-more" style="left:481px;top:160px"><svg width="7" height="7" viewBox="0 0 8 8"><circle cx="4" cy="4" r="3.4" fill="none" stroke="#333"/><path d="M2 4h4M4.3 2.5 6 4 4.3 5.5" fill="none" stroke="#333"/></svg>Read More</div>
  </section>

  <h2 class="section-title" style="top:726px">Project Approach</h2>

  <div class="approach-icon" style="left:95px;top:784px" role="img" aria-label="Icon of classical columns for the three pillars"><span></span></div>
  <h3 class="approach-title" style="left:171px;top:787px">Three Pillars</h3>
  <ul class="approach-list" style="left:171px;top:802px"><li>Maintenance &amp; Reliability</li><li>Inventory &amp; Stores</li><li>Procurement &amp; Payables</li></ul>

  <div class="approach-icon" style="left:277px;top:784px" role="img" aria-label="Icon of three linked arrow panels for the three phases"><span></span></div>
  <h3 class="approach-title" style="left:357px;top:787px">Three Phases</h3>
  <ul class="approach-list" style="left:357px;top:802px"><li>Pre-Feasibility</li><li>Feasibility</li><li>Execution</li></ul>

  <div class="approach-icon" style="left:452px;top:784px" role="img" aria-label="Icon of overlapping circles for the three dimensions"><span></span></div>
  <h3 class="approach-title" style="left:532px;top:787px">Three Dimensions</h3>
  <ul class="approach-list" style="left:532px;top:802px"><li>People &amp; Process</li><li>Physical</li><li>Technical</li></ul>

  <section class="testimonials">
    <h2 class="section-title" style="top:22px">Testimonials</h2>
  </section>
  <div class="avatar" role="img" aria-label="Portrait photo of the client giving the testimonial"></div>
  <p class="quote">Lorem ipsum dolor sit amet, consectetuer adipiscing elit. Aenean commodo ligula<br>eget dolor. Aenean massa. Cum sociis natoque penatibus et magnis dis parturient<br>montes, nascetur &nbsp;montes, nascetur ridiculus Lorem</p>
  <p class="quote-author">- Dana Rolfe</p>

  <footer class="site-footer">
    <h4 class="footer-heading" style="left:94px">Quick links</h4>
    <ul class="quick-links"><li>Home</li><li>What We Do</li><li>How We do it</li><li>Who Are We?</li><li>Software</li><li>Partnerships</li><li>Contact</li></ul>

    <h4 class="footer-heading" style="left:261px">Address</h4>
    <div class="address-row" style="left:261px;top:38px"><svg width="11" height="16" viewBox="0 0 11 16"><path d="M5.5 16C2 10 0 8 0 5.5a5.5 5.5 0 0 1 11 0C11 8 9 10 5.5 16z" fill="#eee"/></svg><span>Lorem ipsum dolor sit amet<br>consectetuer adipiscing</span></div>
    <div class="address-row" style="left:262px;top:69px;font-size:9.5px"><svg width="9" height="9" viewBox="0 0 10 10"><path d="M2 0 4 3 3 4.3Q4.5 6.5 5.7 7L7 6l3 2-1.5 2Q3 9.5 0 1.5z" fill="#eee"/></svg><span>555.014.2280</span></div>
    <div class="address-row" style="left:262px;top:92px"><svg width="10" height="8" viewBox="0 0 10 8"><rect width="10" height="8" fill="#eee"/><path d="M0 0 5 4.5 10 0" fill="none" stroke="#3a3a3c"/></svg><span>info@tallpineupkeep.com</span></div>

    <h4 class="footer-heading" style="left:456px">Newsletter</h4>
    <p class="newsletter-note">Enter your email address below to subscribe .</p>
    <div class="subscribe"><div class="subscribe-input">Enter your email</div><div class="subscribe-btn">SUBSCRIBE</div></div>
    <div class="social" style="left:456px;background:#5b86b8" aria-label="Photo sharing profile"></div>
    <div class="social" style="left:476px;background:#1da1f2" aria-label="Microblog profile"></div>

    <p class="copyright">Copyright © 2017 . All rights reserved.</p>
  </footer>

  <svg class="to-top" viewBox="0 0 19 19" aria-label="Back to top"><circle cx="9.5" cy="9.5" r="9.5" fill="#9a9a9a"/><path d="M5 11.5 9.5 7 14 11.5" fill="none" stroke="#fff" stroke-width="2"/></svg>
</div>
</body>
</html>
```